Brightfold Systems - IT Service and Consulting
Business Card, Letterhead, Envelopes, Fax templates, and CD Label
Brightfold Systems - IT Service and Consulting -
Creative Brief
Professional
Mara Pellin
Owner
517 W. Orchard Gate Ave #216 Orchard Gate, CA 90482
MPellin@BrightfoldSystems.Com
www.brightfoldsystems.com
We want to communicate that Brightfold Systems is a professional IT Service and Consulting Firm. We want a stationary that conveys professionalism and confidence, at the same time we want to appear unique and approachable to small businesses.
Back should be used to convey the company logo, tagline, and URL.

```html
<!DOCTYPE html>
<html lang="en">
<head>
<meta charset="utf-8">
<title>Brightfold Systems — Stationery Set</title>
<link href="https://fonts.googleapis.com/css2?family=Open+Sans:wght@400;600;700&display=swap" rel="stylesheet">
<style>
  :root {
    --stage: #3b3c3e;
    --paper: #ffffff;
    --brand-blue: #1f4f9f;
    --ink: #4a4a4a;
    --ink-soft: #8a8a8a;
    --envelope-dark: #4b4c4e;
    --caption: #9a9a9a;
  }
  * { box-sizing: border-box; margin: 0; padding: 0; }
  html, body { width: 1200px; height: 439px; overflow: hidden; }
  body {
    background: var(--stage);
    font-family: "Open Sans", Arial, sans-serif;
    position: relative;
    color: var(--ink);
  }
  .piece {
    position: absolute;
    background: var(--paper);
    overflow: hidden;
    box-shadow: 0 2px 6px rgba(0,0,0,.45);
  }
  .caption {
    position: absolute;
    font-size: 6px;
    color: var(--caption);
    text-align: center;
  }
  .brand {
    display: flex;
    align-items: center;
    gap: 5px;
    font-weight: 700;
    color: var(--brand-blue);
    white-space: nowrap;
  }
  .brand-dot {
    border-radius: 50%;
    background: var(--brand-blue);
    flex: none;
  }
  .brand--white { color: var(--paper); }
  .brand--white .brand-dot { background: var(--paper); }
  .small { font-size: 4px; line-height: 1.5; color: var(--ink-soft); }
  .rule { position: absolute; height: 1px; background: var(--brand-blue); }

  /* Business cards */
  .card { left: 19px; width: 154px; }
  .card-front { top: 65px; height: 91px; }
  .card-front .brand { position: absolute; left: 10px; top: 12px; font-size: 11px; }
  .card-front .brand-dot { width: 14px; height: 14px; }
  .card-front .contact { position: absolute; left: 10px; top: 50px; }
  .card-front .person { position: absolute; right: 8px; top: 12px; text-align: right; }
  .person-name { font-size: 5px; font-weight: 700; color: var(--brand-blue); }

  .card-back-white { top: 187px; height: 96px; }
  .card-back-white .brand { position: absolute; right: 10px; top: 38px; font-size: 11px; }
  .card-back-white .brand-dot { width: 14px; height: 14px; }

  .card-back-blue { top: 305px; height: 103px; background: var(--brand-blue); }
  .card-back-blue .brand { position: absolute; left: 20px; top: 34px; font-size: 11px; }
  .card-back-blue .brand-dot { width: 14px; height: 14px; }
  .card-back-blue .tagline { position: absolute; left: 39px; top: 56px; font-size: 4.5px; letter-spacing: .5px; color: #dce5f4; }
  .card-back-blue .url { position: absolute; left: 39px; top: 63px; font-size: 4.5px; color: #dce5f4; }

  /* Letterheads */
  .letterhead { top: 24px; width: 288px; height: 384px; }
  .letterhead-a { left: 204px; }
  .letterhead-b { left: 509px; width: 283px; }
  .letterhead .brand-dot { width: 18px; height: 18px; }
  .letterhead-a .brand { position: absolute; left: 16px; top: 14px; font-size: 14px; }
  .letterhead-a .address { position: absolute; left: 16px; top: 42px; }
  .letterhead-a .footer { position: absolute; left: 16px; bottom: 10px; font-size: 4px; color: var(--brand-blue); }
  .letterhead .rule { left: 16px; right: 16px; bottom: 20px; }
  .letterhead-b .brand { position: absolute; left: 50%; transform: translateX(-50%); top: 18px; font-size: 14px; }
  .letterhead-b .footer { position: absolute; left: 0; right: 0; bottom: 10px; text-align: center; font-size: 4px; color: var(--ink-soft); }

  /* Envelopes */
  .envelope { left: 816px; width: 372px; }
  .envelope svg { position: absolute; left: 0; top: 0; }
  .env-dark { top: 19px; height: 101px; background: #f2f2f2; }
  .env-blue { top: 91px; height: 113px; background: #f4f4f4; }
  .env-white { top: 180px; height: 108px; background: #f7f7f7; }
  .env-front { top: 257px; left: 804px; width: 384px; height: 132px; }
  .flap-logo { position: absolute; left: 50%; transform: translateX(-50%); }
  .flap-logo .brand-dot { width: 16px; height: 16px; }
  .env-url { position: absolute; left: 0; right: 0; text-align: center; font-size: 4px; color: var(--ink-soft); }
  .env-front .brand { position: absolute; left: 12px; top: 10px; font-size: 10px; }
  .env-front .brand-dot { width: 12px; height: 12px; }
  .env-front .address { position: absolute; left: 12px; top: 28px; }
</style>
</head>
<body>

  <section class="piece card card-front">
    <div class="brand"><span class="brand-dot"></span>Brightfold</div>
    <div class="person">
      <div class="person-name">Mara Pellin</div>
      <div class="small">Owner</div>
    </div>
    <div class="contact small">
      517 W. Orchard Gate Ave #216<br>
      Orchard Gate, CA 90482<br>
      MPellin@BrightfoldSystems.Com<br>
      www.brightfoldsystems.com
    </div>
  </section>
  <p class="caption" style="left:19px;width:154px;top:165px;">Front Card Option 1</p>

  <section class="piece card card-back-white">
    <div class="brand"><span class="brand-dot"></span>Brightfold</div>
  </section>
  <p class="caption" style="left:19px;width:154px;top:290px;">Back Card Option 1</p>

  <section class="piece card card-back-blue">
    <div class="brand brand--white"><span class="brand-dot"></span>Brightfold Systems</div>
    <div class="tagline">IT SERVICE AND CONSULTING</div>
    <div class="url">www.brightfoldsystems.com</div>
  </section>
  <p class="caption" style="left:19px;width:154px;top:416px;">Back Card Option 2</p>

  <section class="piece letterhead letterhead-a">
    <div class="brand"><span class="brand-dot"></span>Brightfold Systems</div>
    <div class="address small">
      517 W. Orchard Gate Ave #216<br>
      Orchard Gate, CA 90482<br>
      MPellin@BrightfoldSystems.Com
    </div>
    <div class="rule"></div>
    <div class="footer">www.brightfoldsystems.com</div>
  </section>
  <p class="caption" style="left:204px;width:288px;top:418px;">Letterhead Option A</p>

  <section class="piece letterhead letterhead-b">
    <div class="brand"><span class="brand-dot"></span>Brightfold Systems</div>
    <div class="rule"></div>
    <div class="footer">517 W. Orchard Gate Ave #216 Orchard Gate, CA 90482 · www.brightfoldsystems.com</div>
  </section>
  <p class="caption" style="left:509px;width:283px;top:418px;">Letterhead Option B</p>

  <section class="piece envelope env-dark">
    <svg width="372" height="101" viewBox="0 0 372 101">
      <polygon points="0,0 372,0 186,62" fill="var(--envelope-dark)"/>
    </svg>
    <div class="flap-logo brand brand--white" style="top:16px;"><span class="brand-dot"></span></div>
    <div class="env-url" style="top:80px;">www.brightfoldsystems.com</div>
  </section>

  <section class="piece envelope env-blue">
    <svg width="372" height="113" viewBox="0 0 372 113">
      <polygon points="0,0 372,0 186,66" fill="var(--brand-blue)"/>
    </svg>
    <div class="flap-logo brand brand--white" style="top:18px;"><span class="brand-dot"></span></div>
    <div class="env-url" style="top:92px;">www.brightfoldsystems.com</div>
  </section>

  <section class="piece envelope env-white">
    <svg width="372" height="108" viewBox="0 0 372 108">
      <polygon points="0,0 372,0 186,64" fill="#ffffff" stroke="#d8d8d8" stroke-width="1"/>
    </svg>
    <div class="flap-logo brand" style="top:20px;"><span class="brand-dot"></span></div>
  </section>

  <section class="piece envelope env-front">
    <div class="brand"><span class="brand-dot"></span>Brightfold Systems</div>
    <div class="address small">
      517 W. Orchard Gate Ave #216<br>
      Orchard Gate, CA 90482
    </div>
  </section>
  <p class="caption" style="left:816px;width:372px;top:404px;">Envelope Front &amp; Back</p>

</body>
</html>
```